Artificial intelligence company needs icons refresh for its desktop software

Who are we?
We are a company specializing in Artificial Intelligence at the edge, that is to say: Machine Learning on microcontrollers. Our product, PicoForge M LBench, lets developers automatically build an AI library, without any knowledge of machine learning or data science.

What do we need?
We want to refresh our current icons, so we ask you to provide us with a new icon design in SVG format while respecting the overall design of our software. In the attached document you will find screenshots of our software, followed by the current version of the icons that we want to improve. All icons should be provided to us in SVG.
Regarding the 7 icons (Global settings, Regular / Abnormal signals, Signals, optimize and benchmark, Emulator and deploy) we would like a simple animation when the user moves his cursor over the icon in question, so a .gif will suit us as well.

Description of the 7 main icons:
- Global settings: these are the parameters of the project in question, they are a mandatory step of every project and define the boundaries of the project. (Specific platform and resources allocation)
- Regular signals: this is where the user uploads a file describing the usual (normal) operation of a machine (concrete example: the coffee machine is working)
- Abnormal signals: this is where the user uploads a file describing the abnormal operation of the machine (example: the coffee machine is scaled up and the coffee no longer flows)
- Signals: This is where the user uploads files describing several states (for example the coffee machine is scaled up, the coffee machine lacks coffee beans, the coffee machine has no more water, ...).
- Optimize and Benchmark: this is where the magic happens, our software engine will search for the best configuration (library) among an infinite number of possible permutations.
- Emulator: We let the user test the configuration (library) that the Software engine has provided.
- Deploy: This is the last stage of any project, the library suits the user, and they want to download it and deploy it on their microcontrollers.

Requirements
Must have
• Please use dark background to show us your design proposition (we don't want to change the actual dark blue background)
The 7 icons should have a short animated version (GIF) for mouse "hover"

```html
<!DOCTYPE html>
<html lang="en">
<head>
<meta charset="utf-8">
<title>PicoForge M LBench – Workflow Icons</title>
<link rel="stylesheet" href="https://fonts.googleapis.com/css2?family=Montserrat:wght@400;500&display=swap">
<style>
  :root {
    --page-bg: #000000;
    --band-bg: #536874;
    --band-glow: #5f7d90;
    --accent: #5bc8f2;
    --ink: #ffffff;
    --track: #d9dee2;
  }
  * { margin: 0; padding: 0; box-sizing: border-box; }
  html, body {
    width: 1200px; height: 1112px; overflow: hidden;
    background: var(--page-bg);
    font-family: "Montserrat", Arial, sans-serif;
  }
  .workflow-band {
    position: absolute; left: 0; top: 425px;
    width: 1200px; height: 268px;
    background: radial-gradient(ellipse 260px 160px at 600px 20px, var(--band-glow), var(--band-bg));
  }
  .timeline-track {
    position: absolute; left: 121px; right: 93px; top: 214px;
    height: 2px; background: var(--track);
  }
  .step {
    position: absolute; top: 0; width: 200px; margin-left: -100px;
    display: flex; flex-direction: column; align-items: center;
  }
  .step-icon { width: 80px; height: 80px; margin-top: 60px; }
  .step-label {
    margin-top: 7px; color: var(--ink);
    font-size: 13.5px; font-weight: 400; letter-spacing: 0.1px;
    white-space: nowrap;
  }
  .step-node {
    position: absolute; top: 201px;
    width: 28px; height: 28px; border-radius: 50%;
    border: 2px solid var(--track); background: var(--band-bg);
  }
  .accent { fill: var(--accent); }
  .ink { fill: var(--ink); }
  .accent-line { stroke: var(--accent); fill: none; }
  .ink-line { stroke: var(--ink); fill: none; }
</style>
</head>
<body>
<section class="workflow-band">
  <div class="timeline-track"></div>

  <div class="step" style="left:107px">
    <svg class="step-icon" viewBox="0 0 80 80" aria-label="Global Setting">
      <g transform="translate(46 34)">
        <g class="accent">
          <rect x="-5" y="-31" width="10" height="62" rx="1"/>
          <rect x="-5" y="-31" width="10" height="62" rx="1" transform="rotate(45)"/>
          <rect x="-5" y="-31" width="10" height="62" rx="1" transform="rotate(90)"/>
          <rect x="-5" y="-31" width="10" height="62" rx="1" transform="rotate(135)"/>
          <circle r="24"/>
        </g>
        <circle class="ink" r="8.5"/>
        <circle r="5" fill="var(--band-bg)" opacity="0"/>
      </g>
      <g transform="translate(17 61)">
        <g class="ink">
          <rect x="-3" y="-15" width="6" height="30" rx="1"/>
          <rect x="-3" y="-15" width="6" height="30" rx="1" transform="rotate(45)"/>
          <rect x="-3" y="-15" width="6" height="30" rx="1" transform="rotate(90)"/>
          <rect x="-3" y="-15" width="6" height="30" rx="1" transform="rotate(135)"/>
          <circle r="11"/>
        </g>
        <circle r="4" fill="var(--band-bg)"/>
      </g>
    </svg>
    <span class="step-label">Global Setting</span>
  </div>

  <div class="step" style="left:304px">
    <svg class="step-icon" viewBox="0 0 80 80" aria-label="Regular Signal">
      <circle class="accent-line" cx="35" cy="24" r="19" stroke-width="3"/>
      <circle class="accent-line" cx="35" cy="24" r="12" stroke-width="3"/>
      <path class="ink" d="M31 24 h8 l12 36 h-7 l-9 -27 l-9 27 h-7 z"/>
      <circle class="ink" cx="35" cy="24" r="5"/>
      <circle class="accent" cx="61" cy="47" r="9"/>
      <path class="ink-line" d="M56.5 47 l3 3 l6 -6" stroke-width="2.4" stroke-linecap="round" stroke-linejoin="round"/>
    </svg>
    <span class="step-label">Regular Signal</span>
  </div>

  <div class="step" style="left:501px">
    <svg class="step-icon" viewBox="0 0 80 80" aria-label="Abnormal Signal">
      <path class="ink" d="M31 22 h8 l12 38 h-7 l-9 -29 l-9 29 h-7 z"/>
      <circle class="ink" cx="35" cy="21" r="5"/>
      <circle class="accent" cx="59" cy="43" r="9"/>
      <path class="ink-line" d="M55.5 39.5 l7 7 M62.5 39.5 l-7 7" stroke-width="2.4" stroke-linecap="round"/>
    </svg>
    <span class="step-label">Abnormal Signal</span>
  </div>

  <div class="step" style="left:698px">
    <svg class="step-icon" viewBox="0 0 80 80" aria-label="Optimize and Benchmark">
      <path class="ink-line" d="M4 2 V76 H78" stroke-width="4"/>
      <rect class="accent" x="14" y="30" width="10" height="40"/>
      <rect class="accent" x="29" y="40" width="10" height="30"/>
      <rect class="accent" x="44" y="34" width="10" height="36"/>
      <rect class="accent" x="59" y="10" width="10" height="60"/>
    </svg>
    <span class="step-label">Optimize and Benchmark</span>
  </div>

  <div class="step" style="left:896px">
    <svg class="step-icon" viewBox="0 0 80 80" aria-label="Emulator">
      <rect class="ink" x="3" y="6" width="74" height="57" rx="2"/>
      <rect class="accent" x="9" y="12" width="62" height="45"/>
      <rect class="ink" x="9" y="26" width="62" height="7"/>
      <rect class="accent" x="29" y="63" width="22" height="8"/>
      <rect class="ink" x="17" y="71" width="46" height="5"/>
    </svg>
    <span class="step-label">Emulator</span>
  </div>

  <div class="step" style="left:1093px">
    <svg class="step-icon" viewBox="0 0 80 80" aria-label="Deploy">
      <g transform="translate(40 40)">
        <g class="accent-line" stroke-width="3">
          <line x1="0" y1="0" x2="0" y2="-32"/>
          <line x1="0" y1="0" x2="0" y2="-32" transform="rotate(45)"/>
          <line x1="0" y1="0" x2="0" y2="-32" transform="rotate(90)"/>
          <line x1="0" y1="0" x2="0" y2="-32" transform="rotate(135)"/>
          <line x1="0" y1="0" x2="0" y2="-32" transform="rotate(180)"/>
          <line x1="0" y1="0" x2="0" y2="-32" transform="rotate(225)"/>
          <line x1="0" y1="0" x2="0" y2="-32" transform="rotate(270)"/>
          <line x1="0" y1="0" x2="0" y2="-32" transform="rotate(315)"/>
        </g>
        <g class="accent">
          <circle cy="-33" r="4.5"/>
          <circle cy="-33" r="4.5" transform="rotate(45)"/>
          <circle cy="-33" r="4.5" transform="rotate(90)"/>
          <circle cy="-33" r="4.5" transform="rotate(135)"/>
          <circle cy="-33" r="4.5" transform="rotate(180)"/>
          <circle cy="-33" r="4.5" transform="rotate(225)"/>
          <circle cy="-33" r="4.5" transform="rotate(270)"/>
          <circle cy="-33" r="4.5" transform="rotate(315)"/>
        </g>
        <circle class="ink" r="14"/>
      </g>
    </svg>
    <span class="step-label">Deploy</span>
  </div>

  <span class="step-node" style="left:93px"></span>
  <span class="step-node" style="left:290px"></span>
  <span class="step-node" style="left:487px"></span>
  <span class="step-node" style="left:684px"></span>
  <span class="step-node" style="left:882px"></span>
  <span class="step-node" style="left:1079px"></span>
</section>
</body>
</html>
```